Polish brewery needs BEER LABEL design for WEDDINGS

We need beer label design for weddings. Our brewery is located on South of Poland and it is called Wytwórnia Orlik [PL]/Factory Falcon [ENG]. We feel strong connection to mountains and we use water from the mountain in our vicinity.
Regarding beer style it is India Pale Ale so beer is bitter and aromatic because of high addition of hops. Label design has to be modern and simple. We would prefer bright and cream colors.
We need to have opportunity to edit data which are on the label so we will need to get appropriate files.
In attached files you can find all details. If any additional information will be required please do not hesitate and contact with me.

Target Market(s)

Weddings

Font styles to use
Sans Serif
Script

Colors
ffffff

Requirements
Must have
• Information listed in documents in attached files
Nice to have
• Some nice graphics
Bright and cream colors.
Should not have
• -

```html
<!DOCTYPE html>
<html lang="pl">
<head>
<meta charset="utf-8">
<title>Etykieta weselna – India Pale Ale</title>
<link rel="stylesheet" href="https://fonts.googleapis.com/css2?family=Great+Vibes&family=Poppins:wght@400;600&family=Yanone+Kaffeesatz:wght@400&display=swap">
<style>
  :root{
    --page:#efeeeb;
    --paper:#ffffff;
    --ink:#3b3631;
    --gold:#8a6d45;
    --gold-soft:#c9b796;
    --cream:#f4efe3;
    --cream-deep:#e9dfc9;
    --blush:#e8c2b0;
  }
  *{box-sizing:border-box;margin:0;padding:0}
  html,body{width:1200px;height:886px;overflow:hidden}
  body{background:var(--page);font-family:"Poppins",sans-serif;color:var(--ink);position:relative}
  .label{position:absolute;left:30px;top:190px;width:1140px;height:506px;background:var(--paper);box-shadow:0 2px 10px rgba(0,0,0,.12)}
  .abs{position:absolute}
  .rule{position:absolute;height:0;border-top:2px solid var(--gold)}
  .rule.dotted{border-top:1.5px dotted var(--gold)}
  .col-left{left:24px;width:255px}
  .col-right{left:858px;width:254px}
  .ingredients{top:34px;font-size:16px;line-height:21px;text-align:justify;text-align-last:left}
  .volume{top:120px;display:flex;align-items:center;gap:16px}
  .volume-label{font-size:13px;line-height:16px}
  .volume-value{font-size:26px;color:var(--gold)}
  .best-before{top:178px;font-size:14px;line-height:19px}
  .batch-box{top:226px;height:72px;border:1.5px dotted var(--gold)}
  .storage{top:306px;font-size:14px;line-height:18px}
  .address{top:360px;font-size:14px;line-height:18.5px;width:170px}
  .maker{top:368px;left:208px;width:72px;text-align:center;font-size:13px;line-height:15px;color:var(--gold)}
  .maker-mark{display:block;width:28px;height:28px;background:var(--gold);margin:0 auto 8px}
  .vsep{position:absolute;top:366px;left:196px;height:104px;border-left:1.5px dotted var(--gold)}
  .art{left:306px;top:22px;width:522px;height:456px;border-radius:48% 48% 30% 30%;background:radial-gradient(ellipse at 50% 45%,var(--cream) 0%,#f7f1e6 45%,#fbf8f2 70%,var(--paper) 100%)}
  .art-side{top:120px;width:70px;height:280px;border-radius:40px;background:linear-gradient(180deg,var(--blush),var(--cream-deep));opacity:.55}
  .couple{left:306px;width:522px;top:180px;text-align:center;font-family:"Great Vibes",cursive;font-size:62px;line-height:80px;color:var(--gold)}
  .date{left:306px;width:522px;top:252px;text-align:center;font-size:23px;color:var(--ink)}
  .banner{left:388px;top:418px;width:362px;height:58px;border:2px solid var(--gold);border-radius:14px;background:linear-gradient(180deg,#fbf9f3,var(--cream));display:flex;align-items:center;justify-content:center;font-family:"Yanone Kaffeesatz",sans-serif;font-size:36px;color:var(--gold)}
  .story{top:34px;font-size:16px;line-height:21.4px;text-align:justify}
  .stats{top:266px;height:76px;display:flex}
  .stat{flex:1;display:flex;flex-direction:column;align-items:center;gap:8px;font-size:12px;font-weight:600}
  .stat+.stat{border-left:1.5px dotted var(--gold)}
  .stat .source{font-size:10px;line-height:10px;text-align:center}
  .drop{width:28px;height:28px;border-radius:50%;background:var(--gold)}
  .dots{display:flex;gap:4px}
  .dots i{width:15px;height:20px;border-radius:50%;background:var(--gold)}
  .dots i.off{background:var(--gold-soft);opacity:.6}
  .bars{display:flex;gap:6px}
  .bars i{width:8px;height:24px;border-radius:4px;background:var(--gold)}
  .bars i.off{background:var(--gold-soft);opacity:.6}
  .strength{top:356px;display:flex;align-items:center;font-size:21px}
  .strength span{flex:1;text-align:center}
  .strength span+span{border-left:1.5px dotted var(--gold)}
  .links{top:404px;font-size:13.5px;font-weight:600;line-height:22px}
  .links li{list-style:none;display:flex;align-items:center;gap:12px}
  .links li::before{content:"";width:13px;height:13px;border-radius:50%;background:var(--ink)}
</style>
</head>
<body>
<section class="label" aria-label="Etykieta piwa weselnego India Pale Ale">

  <!-- left column -->
  <div class="rule col-left" style="top:22px"></div>
  <p class="abs col-left ingredients">Składniki: woda, słód jęczmienny, chmiel, liście limonki, drożdże.</p>
  <div class="rule dotted col-left" style="top:112px"></div>
  <div class="abs col-left volume">
    <span class="volume-label">Objętość<br>butelki:</span>
    <span class="volume-value">330 ml</span>
  </div>
  <div class="rule col-left" style="top:169px"></div>
  <p class="abs col-left best-before">Najlepiej spożyć przed:<br>Data stanowi numer partii</p>
  <div class="abs col-left batch-box"></div>
  <p class="abs col-left storage">Przechowywać w suchym<br>i chłodnym miejscu</p>
  <div class="rule col-left" style="top:352px"></div>
  <p class="abs col-left address">Wytwórnia Orlik<br>34-400 Jodłowa Dolina<br>Browar Klasztorny<br>Sokół<br>Zagórze 12, 34-600<br>Zagórze</p>
  <div class="vsep" style="left:220px"></div>
  <div class="abs maker" style="left:224px;width:60px"><span class="maker-mark"></span>Wytwórnia Orlik</div>
  <div class="rule col-left" style="top:481px"></div>

  <!-- centre artwork -->
  <div class="abs art" role="img" aria-label="Ornamentalna rama ze złotych zawijasów, liści chmielu i białych lilii"></div>
  <div class="abs art-side" style="left:330px" role="img" aria-label="Pnące łodygi z liśćmi po lewej stronie"></div>
  <div class="abs art-side" style="left:734px" role="img" aria-label="Pnące łodygi z liśćmi po prawej stronie"></div>
  <h1 class="abs couple">Alina &amp; Tomasz</h1>
  <p class="abs date">20.06.2020</p>
  <div class="abs banner">India Pale Ale</div>

  <!-- right column -->
  <div class="rule col-right" style="top:22px"></div>
  <p class="abs col-right story">Trzymasz w ręku naszą autorską IPA do produkcji której wykorzystujemy wodę wypływającą z samego serca Beskidu Wysokiego – Babiej Góry. IPA lubi chmiele i goryczkę, ale żeby nie było nudno postanowiliśmy ją wzbogacić limonką.</p>
  <div class="rule col-right" style="top:258px"></div>
  <div class="abs col-right stats">
    <div class="stat"><span class="source">BABIA<br>GÓRA</span><span class="drop"></span></div>
    <div class="stat">IBU<span class="dots"><i></i><i></i><i class="off"></i></span></div>
    <div class="stat">EBC<span class="bars"><i></i><i class="off"></i><i class="off"></i></span></div>
  </div>
  <div class="rule col-right" style="top:348px"></div>
  <div class="abs col-right strength"><span>ALK 5,5 %</span><span>EXT 14 %</span></div>
  <div class="rule col-right" style="top:396px"></div>
  <ul class="abs col-right links">
    <li>wytworniaorlik</li>
    <li>orlikbrew</li>
    <li>www.wytworniaorlik.pl</li>
  </ul>
  <div class="rule col-right" style="top:481px"></div>
</section>
</body>
</html>
```